Bref créative
Business Card/Stationary for Orthodontic Practice
Kellin Orthodontics
Simple
Darek P. Kellin, DDS, MS, LLC
Specialist in Braces for Children and Adults
Two addresses:
WHEATON OFFICE:
48752 Corvane Ave.
Suite 101
Wheaton, MD 20902
SILVER SPRING OFFICE:
26419 Old Brisbury Ave.
Silver Spring, MD 20904
see above in address section
DrKellin@kellinortho.example
www.KellinOrtho.example

```html
<!DOCTYPE html>
<html lang="en">
<head>
<meta charset="utf-8">
<title>Kellin Orthodontics Stationery</title>
<link href="https://fonts.googleapis.com/css2?family=Open+Sans:wght@400;600&display=swap" rel="stylesheet">
<style>
:root{
  --navy:#1d3a6b;
  --blue:#1f5fa8;
  --blue-dark:#173f78;
  --green:#7cc243;
  --grey:#6f7780;
  --paper:#ffffff;
  --stage:#eceeef;
}
*{box-sizing:border-box;margin:0;padding:0}
html,body{width:1200px;height:936px;overflow:hidden;background:var(--stage);font-family:"Open Sans",Arial,sans-serif}
.canvas{position:relative;width:1200px;height:936px}
.sheet{position:absolute;background:var(--paper);box-shadow:0 1px 4px rgba(0,0,0,.12);overflow:hidden}
.brand{position:absolute;display:flex;align-items:center;gap:8px;white-space:nowrap}
.brand-dot{border-radius:50%;background:var(--green);flex:none}
.brand-name{font-family:"Open Sans",Arial,sans-serif;font-weight:600;color:var(--navy);line-height:1}
.tagline{position:absolute;font-family:"Open Sans",Arial,sans-serif;font-weight:400;color:var(--grey);white-space:nowrap}
.footer-band{position:absolute;left:0;bottom:0;width:100%}
.contact{position:absolute;font-size:6px;line-height:1.55;color:var(--grey)}
.contact li{list-style:none;display:flex;align-items:center;gap:3px;white-space:nowrap}
.contact li::before{content:"";width:4px;height:4px;border-radius:50%;background:var(--blue);flex:none}

.letterhead{left:178px;top:56px;width:418px;height:555px}
.letterhead .brand{left:30px;top:30px}
.letterhead .brand-dot{width:12px;height:12px}
.letterhead .brand-name{font-size:13px}
.letterhead .tagline{left:50px;top:50px;font-size:7px}
.letterhead .contact{left:298px;top:22px}
.watermark{position:absolute;left:149px;top:250px;width:120px;height:120px;border-radius:50%;background:rgba(124,194,67,.08)}

.folder{left:634px;top:38px;width:462px;height:576px}
.folder .brand{left:82px;top:276px}
.folder .brand-dot{width:24px;height:24px}
.folder .brand-name{font-size:26px}
.folder .tagline{left:116px;top:316px;font-size:12px}

.card{width:198px;height:112px}
.card-front{left:43px;top:655px}
.card-front .brand{left:12px;top:14px}
.card-front .brand-dot{width:8px;height:8px}
.card-front .brand-name{font-size:9px}
.card-front .tagline{left:28px;top:28px;font-size:5px}
.card-front .contact{left:12px;top:52px;font-size:4.5px}
.card-front .contact li::before{width:3px;height:3px}
.card-back{left:43px;top:781px}
.card-back .brand{left:92px;top:38px}
.card-back .brand-dot{width:14px;height:14px}
.card-back .web{position:absolute;left:0;width:100%;top:68px;text-align:center;font-size:6px;color:var(--blue-dark);letter-spacing:.05em}

.envelope{width:434px;height:223px}
.env-front{left:266px;top:665px}
.env-front .brand{left:18px;top:24px}
.env-front .brand-dot{width:11px;height:11px}
.env-front .brand-name{font-size:12px}
.env-front .tagline{left:37px;top:42px;font-size:6px}
.env-back{left:736px;top:665px}
.flap{position:absolute;left:0;top:0;width:100%}
.flap-web{position:absolute;left:0;width:100%;top:30px;text-align:center;color:#fff;font-size:10px;letter-spacing:.3em}
</style>
</head>
<body>
<main class="canvas">

  <section class="sheet letterhead">
    <div class="brand"><span class="brand-dot"></span><span class="brand-name">Kellin Orthodontics</span></div>
    <div class="tagline">Specialist in Braces</div>
    <ul class="contact">
      <li>48752 Corvane Ave., Suite 101</li>
      <li>Wheaton, MD 20902</li>
      <li>26419 Old Brisbury Ave.</li>
      <li>Silver Spring, MD 20904</li>
      <li>301-555-0142</li>
      <li>DrKellin@kellinortho.example</li>
    </ul>
    <div class="watermark" role="img" aria-label="Faint brand decoration area"></div>
    <svg class="footer-band" viewBox="0 0 418 18" preserveAspectRatio="none" height="18">
      <defs><linearGradient id="bandBlue" x1="0" x2="1"><stop offset="0" stop-color="#173f78"/><stop offset="1" stop-color="#2a7cc6"/></linearGradient></defs>
      <rect x="0" y="2" width="418" height="1" fill="#2a7cc6"/>
      <polygon points="0,6 290,6 278,18 0,18" fill="url(#bandBlue)"/>
      <polygon points="294,6 418,6 418,18 282,18" fill="#7cc243"/>
    </svg>
  </section>

  <section class="sheet folder">
    <div class="brand"><span class="brand-dot"></span><span class="brand-name">Kellin Orthodontics</span></div>
    <div class="tagline">Specialist in Braces</div>
    <svg class="footer-band" viewBox="0 0 462 22" preserveAspectRatio="none" height="22">
      <defs><linearGradient id="bandBlue2" x1="0" x2="1"><stop offset="0" stop-color="#173f78"/><stop offset="1" stop-color="#2a7cc6"/></linearGradient></defs>
      <rect x="0" y="2" width="462" height="1.2" fill="#2a7cc6"/>
      <polygon points="0,7 320,7 306,22 0,22" fill="url(#bandBlue2)"/>
      <polygon points="324,7 462,7 462,22 310,22" fill="#7cc243"/>
    </svg>
  </section>

  <section class="sheet card card-front">
    <div class="brand"><span class="brand-dot"></span><span class="brand-name">Kellin Orthodontics</span></div>
    <div class="tagline">Specialist in Braces</div>
    <ul class="contact">
      <li>Darek P. Kellin, DDS, MS, LLC</li>
      <li>48752 Corvane Ave., Wheaton</li>
      <li>26419 Old Brisbury Ave.</li>
      <li>DrKellin@kellinortho.example</li>
    </ul>
    <svg class="footer-band" viewBox="0 0 198 8" preserveAspectRatio="none" height="8">
      <polygon points="0,2 130,2 124,8 0,8" fill="#1f5fa8"/>
      <polygon points="133,2 198,2 198,8 127,8" fill="#7cc243"/>
    </svg>
  </section>

  <section class="sheet card card-back">
    <div class="brand"><span class="brand-dot"></span></div>
    <div class="web">www.KellinOrtho.example</div>
  </section>

  <section class="sheet envelope env-front">
    <div class="brand"><span class="brand-dot"></span><span class="brand-name">Kellin Orthodontics</span></div>
    <div class="tagline">Specialist in Braces</div>
    <svg class="footer-band" viewBox="0 0 434 12" preserveAspectRatio="none" height="12">
      <defs><linearGradient id="bandBlue3" x1="0" x2="1"><stop offset="0" stop-color="#173f78"/><stop offset="1" stop-color="#2a7cc6"/></linearGradient></defs>
      <polygon points="0,2 300,2 292,12 0,12" fill="url(#bandBlue3)"/>
      <polygon points="304,2 434,2 434,12 296,12" fill="#7cc243"/>
    </svg>
  </section>

  <section class="sheet envelope env-back">
    <svg class="flap" viewBox="0 0 434 90" preserveAspectRatio="none" height="90">
      <defs><linearGradient id="flapBlue" x1="0" x2="1"><stop offset="0" stop-color="#173f78"/><stop offset=".5" stop-color="#2a7cc6"/><stop offset="1" stop-color="#173f78"/></linearGradient></defs>
      <path d="M0,0 H434 V60 Q217,100 0,60 Z" fill="url(#flapBlue)"/>
    </svg>
    <div class="flap-web">www.KellinOrtho.example</div>
  </section>

</main>
</body>
</html>
```